Business cards to launch an education platform

Hi,
I am looking at having new business cards designed.
I am a startup, developing a web platform for schools and university, the education world. It's an online assessment system.
I would like a card that looks classy, and that is using the colors and the font of my logo.

I have attached:
1) my logo
2) A business card that I have designed quickly so you can have all the information required in the card, but I really don't like it.
3) The font that I am using (Lato Regular) to design my web platform
4) Some screenshots of my web platform so you can have a look at the style that I have.

Target Market(s)

Major market: Education system: Schools and university
Minor markets: Business in general

Industry/Entity Type

Business

Contact Information for Business Card

Tessa Vinall
Director

M: 0487 312 950
E: tessa.vinall@copperLoomVentures.com.au

Requirements
Must have
• The colors of my logo

```html
<!DOCTYPE html>
<html lang="en">
<head>
<meta charset="utf-8">
<title>Copper Loom Ventures — Business Cards</title>
<link rel="stylesheet" href="https://fonts.googleapis.com/css2?family=Lato:wght@400;700&display=swap">
<style>
  :root {
    --page-bg: #e4e5e6;
    --card-white: #ffffff;
    --card-black: #000000;
    --navy: #0f4a7f;
    --sky: #3bb9e2;
    --brand-blue: #1f5a99;
    --brand-glow: #1e88d6;
    --text-light: #ffffff;
  }
  * { margin: 0; padding: 0; box-sizing: border-box; }
  html, body {
    width: 1189px;
    height: 1200px;
    overflow: hidden;
    background: var(--page-bg);
    font-family: "Lato", sans-serif;
  }
  .canvas { position: relative; width: 1189px; height: 1200px; }
  .card {
    position: absolute;
    left: 136px;
    width: 917px;
    height: 524px;
    overflow: hidden;
  }
  .card--front { top: 45px; background: var(--card-white); }
  .card--back { top: 624px; background: var(--card-black); }

  .brand { position: absolute; display: flex; align-items: center; gap: 28px; }
  .card--front .brand { left: 198px; top: 50px; }
  .card--back .brand { left: 194px; top: 166px; }
  .brand__mark { width: 150px; height: 150px; background: var(--brand-blue); }
  .card--back .brand__mark { background: var(--brand-glow); }
  .brand__name {
    font-weight: 400;
    font-size: 50px;
    line-height: 1.08;
    letter-spacing: 4px;
    color: var(--brand-blue);
  }
  .card--back .brand__name { color: var(--brand-glow); }

  .wave { position: absolute; left: 0; top: 0; width: 917px; height: 524px; }

  .person { position: absolute; left: 39px; top: 365px; color: var(--text-light); }
  .person__name { font-weight: 700; font-size: 50px; line-height: 1; letter-spacing: -0.5px; }
  .person__role { font-weight: 400; font-size: 27px; margin-top: 10px; }

  .divider {
    position: absolute;
    left: 347px;
    top: 362px;
    width: 3px;
    height: 105px;
    background: var(--text-light);
  }

  .contact { position: absolute; left: 383px; top: 388px; list-style: none; color: var(--text-light); }
  .contact__item { display: flex; align-items: center; gap: 14px; font-size: 23px; height: 38px; }
  .contact__icon { width: 20px; height: 20px; flex: none; }
</style>
</head>
<body>
<main class="canvas">
  <section class="card card--front" aria-label="Business card front">
    <div class="brand">
      <div class="brand__mark"></div>
      <div class="brand__name">Copper Loom<br>Ventures</div>
    </div>

    <svg class="wave" viewBox="0 0 917 524" aria-hidden="true">
      <path d="M0 280 C 220 245, 420 285, 600 315 C 730 337, 830 322, 917 284 L917 524 L0 524 Z" fill="var(--sky)"/>
      <path d="M0 289 C 220 255, 420 295, 600 325 C 730 347, 830 332, 917 294 L917 524 L0 524 Z" fill="var(--navy)"/>
    </svg>

    <div class="person">
      <h1 class="person__name">Tessa Vinall</h1>
      <p class="person__role">Director</p>
    </div>

    <div class="divider"></div>

    <ul class="contact">
      <li class="contact__item">
        <svg class="contact__icon" viewBox="0 0 20 20" aria-hidden="true">
          <rect width="20" height="20" rx="2" fill="#fff"/>
          <path d="M6 4 L9 4 L10 7 L8 8.5 C9 11 10 12 12 13 L13.5 11 L16 12 L16 15 C10 15 5 10 6 4 Z" fill="var(--navy)"/>
        </svg>
        <span>0487 312 950</span>
      </li>
      <li class="contact__item">
        <svg class="contact__icon" viewBox="0 0 20 20" aria-hidden="true">
          <rect width="20" height="20" rx="2" fill="#fff"/>
          <rect x="3.5" y="5.5" width="13" height="9" fill="none" stroke="var(--navy)" stroke-width="1.4"/>
          <path d="M3.5 5.5 L10 11 L16.5 5.5" fill="none" stroke="var(--navy)" stroke-width="1.4"/>
        </svg>
        <span>tessa.vinall@copperLoomVentures.com.au</span>
      </li>
    </ul>
  </section>

  <section class="card card--back" aria-label="Business card back">
    <div class="brand">
      <div class="brand__mark"></div>
      <div class="brand__name">Copper Loom<br>Ventures</div>
    </div>
  </section>
</main>
</body>
</html>
```